Design a blog page showing lists of latest posts.

I want to design my blog home page. This page will show a list of my latest blog posts.

The site URL is velrunok.com and I have already given a basic structure to it. Please visit and have a look at it.

The color scheme of the design should be black (or grey) and white.

Below the top header I want an opt-in form and below that list of my blog posts. Then pagination and then a bottom section, that will show my two products. Please design these two boxes without any image.

Please avoid using any background image. If necessary, use any image without a character or person. Avoid using the sidebar.

Make it beautiful with the use of typography and white spaces.

I am open to any new creative ideas. Let me know if you have any?

1 page

• Sidebar

```html
<!DOCTYPE html>
<html lang="en">
<head>
<meta charset="utf-8">
<title>Velrunok — Blog</title>
<link href="https://fonts.googleapis.com/css2?family=Heebo:wght@400;500;700;800&family=Poppins:wght@300;400;500;600;700&display=swap" rel="stylesheet">
<style>
:root{
  --ink:#1e1e1e;
  --dark:#333333;
  --footer:#2b2b2b;
  --text:#555555;
  --muted:#777777;
  --line:#4a4a4a;
  --paper:#ffffff;
  --soft:#f3f3f3;
  --chip:#e6e6e6;
}
*{box-sizing:border-box;margin:0;padding:0}
html,body{width:1200px;height:3130px;overflow:hidden}
body{font-family:'Poppins',sans-serif;color:var(--ink);background:var(--paper);position:relative}
a{color:inherit;text-decoration:none}

/* header */
.site-header{height:84px;background:var(--dark);display:flex;align-items:center;padding:0 118px;justify-content:space-between}
.brand{display:flex;align-items:center;gap:10px;color:#fff;font-family:'Poppins',sans-serif;font-weight:600;font-size:25px}
.brand-dot{width:30px;height:30px;border-radius:50%;background:#e5e5e5}
.main-nav{display:flex;gap:32px;font-size:16px;color:#fff}
.main-nav a.active{text-decoration:underline;text-underline-offset:5px}

/* hero */
.hero{height:511px;background:linear-gradient(160deg,#efefef 0%,#dcdcdc 45%,#ececec 70%,#d8d8d8 100%);text-align:center;padding-top:130px;font-family:'Heebo',sans-serif;position:relative;overflow:hidden}
.hero svg.waves{position:absolute;inset:0}
.hero h1{position:relative;font-size:50px;font-weight:700;color:var(--ink);letter-spacing:-.5px}
.hero p{position:relative;font-size:22px;color:#3a3a3a;line-height:37px;margin-top:10px}
.optin{position:relative;display:flex;width:536px;margin:36px auto 0;height:53px}
.optin .field{flex:1;background:#fff;border:1px solid #5b6b8c;border-right:none;text-align:left;padding:0 21px;display:flex;align-items:center;font-size:17px;color:#666}
.optin .btn{width:182px;background:var(--dark);color:#fff;font-size:17px;display:flex;align-items:center;justify-content:center;border-radius:0 3px 3px 0}

/* posts */
.posts{padding:60px 117px 0}
.posts-head{display:flex;justify-content:space-between;align-items:center;padding-bottom:24px;border-bottom:1.5px solid var(--line)}
.posts-head h2{font-family:'Heebo',sans-serif;font-size:50px;font-weight:400;color:#333}
.posts-head h2 b{font-weight:800}
.category{width:286px;height:42px;background:var(--chip);border-radius:4px;display:flex;align-items:center;justify-content:space-between;padding:0 24px;font-size:16px;color:#333}
.grid{display:grid;grid-template-columns:repeat(3,306px);column-gap:24px;margin-top:46px}
.col{display:flex;flex-direction:column;gap:27px}
.card{background:#fff;box-shadow:0 2px 10px rgba(0,0,0,.08);display:flex;flex-direction:column;height:448px}
.thumb{height:220px;position:relative;flex:none}
.card .thumb.bottom{margin-top:auto}
.date{position:absolute;left:10px;top:10px;width:54px;height:54px;border-radius:50%;background:#fff;font-size:11px;font-weight:600;line-height:12px;display:flex;flex-direction:column;align-items:center;justify-content:center}
.thumb.bottom .date{top:auto;bottom:10px}
.body{padding:22px 25px 0}
.meta{display:flex;justify-content:space-between;font-size:12px;color:var(--muted)}
.body h3{font-size:17px;font-weight:500;line-height:25px;margin-top:12px;color:#222}
.body p{font-size:13.5px;color:var(--muted);line-height:21px;margin-top:10px}
.more{display:block;font-size:13.5px;font-weight:500;margin-top:16px;color:#111}
.t-green{background:linear-gradient(135deg,#5fe05a,#2fb836)}
.t-orange{background:linear-gradient(180deg,#e6871f,#d8771b 55%,#9a9a9a)}
.t-grey{background:linear-gradient(180deg,#f3f4f6,#9a9ea5)}
.t-blue{background:linear-gradient(135deg,#2fc1f0,#0e8bd9)}
.t-paper{background:linear-gradient(135deg,#f4f4f4,#cfd2d2)}
.t-board{background:linear-gradient(180deg,#b8722f 0,#b8722f 4%,#2f5a3f 8%,#264c34 100%)}

.pager{display:flex;justify-content:center;gap:7px;margin-top:60px}
.pager span{width:42px;height:42px;border-radius:50%;border:1px solid #ccc;display:flex;align-items:center;justify-content:center;font-size:14px;color:#666}
.pager .nav{background:#ececec;border-color:#ececec}
.pager .on{background:#3c3c3c;border-color:#3c3c3c;color:#fff}

/* resources */
.resources{position:absolute;top:1912px;left:0;width:1200px;height:853px;background:linear-gradient(180deg,#f2f2f2,#f9f9f9);text-align:center;overflow:hidden}
.resources svg.sweep{position:absolute;inset:0}
.resources h2{position:relative;font-family:'Heebo',sans-serif;font-size:50px;font-weight:400;color:#333;margin-top:75px}
.resources h2 b{font-weight:800}
.resources .lead{position:relative;font-size:17px;color:#444;line-height:30px;margin-top:16px}
.products{position:relative;display:flex;justify-content:center;gap:44px;margin-top:78px}
.product{width:397px;height:450px;background:#fff;padding:18px 18px 0;position:relative}
.product .ph{height:222px}
.product h3{font-size:18px;font-weight:500;margin-top:22px}
.product .by{font-family:'Heebo',sans-serif;font-size:14px;color:#666;margin-top:12px}
.product p{font-family:'Heebo',sans-serif;font-size:14px;color:#333;line-height:21px;margin:16px 28px 0}
.go{position:absolute;left:50%;bottom:-24px;transform:translateX(-50%);width:48px;height:48px;border-radius:50%;background:#111;display:flex;align-items:center;justify-content:center}

/* footer */
.site-footer{position:absolute;top:2765px;left:0;width:1200px;height:365px;background:var(--footer);color:#ddd;padding:62px 118px 0}
.f-cols{display:flex}
.f-col h4{font-size:15px;font-weight:600;color:#fff;margin-bottom:18px}
.contact{width:367px}
.contact li{list-style:none;display:flex;gap:10px;font-size:13.5px;line-height:23px;margin-bottom:14px}
.links{width:270px;padding-top:8px}
.links li{list-style:none;font-size:13.5px;line-height:23px}
.write{padding-top:8px}
.write p{font-size:12.5px;line-height:24px;width:200px}
.sub{display:flex;width:331px;height:38px;margin-top:22px;margin-left:-5px}
.sub .field{flex:1;background:#e9eef2;border-radius:19px 0 0 19px;font-size:13px;color:#888;display:flex;align-items:center;padding-left:24px}
.sub .btn{width:118px;background:#111;color:#fff;font-size:14px;font-weight:600;border-radius:0 19px 19px 0;display:flex;align-items:center;justify-content:center}
.f-bottom{position:absolute;left:118px;right:118px;bottom:45px;display:flex;justify-content:space-between;align-items:center;font-size:13px}
.social{display:flex;gap:8px;background:#3a3a3a;padding:8px 12px;border-radius:3px}
.social i{width:11px;height:11px;border-radius:50%;background:#bbb;display:block}
</style>
</head>
<body>

<header class="site-header">
  <a class="brand" href="#"><span class="brand-dot"></span>Velrunok</a>
  <nav class="main-nav">
    <a class="active" href="#">Home</a><a href="#">PMC Questions</a><a href="#">Contact Hours</a><a href="#">Resources</a><a href="#">Notes</a><a href="#">eBook</a>
  </nav>
</header>

<section class="hero">
  <svg class="waves" width="1200" height="511" viewBox="0 0 1200 511" aria-hidden="true">
    <path d="M0 190 C300 80 520 260 820 150 S1120 60 1200 110 L1200 0 L0 0Z" fill="#fff" opacity=".35"/>
    <path d="M0 511 C250 380 500 470 760 360 S1100 300 1200 330 L1200 511Z" fill="#fff" opacity=".3"/>
    <path d="M450 0 C350 150 320 300 420 511" stroke="#fff" stroke-width="2" fill="none" opacity=".6"/>
    <path d="M1200 380 C1130 420 1110 470 1120 511" stroke="#fff" stroke-width="2" fill="none" opacity=".6"/>
  </svg>
  <h1>Never Miss a Post</h1>
  <p>In the online marketing space, everybody loves the quick win.<br>The shortcut. The "growth hack".</p>
  <form class="optin"><div class="field">Email Address</div><div class="btn">Keep me updated</div></form>
</section>

<section class="posts">
  <div class="posts-head">
    <h2>Latest <b>Posts...</b></h2>
    <div class="category">Category
      <svg width="12" height="8" viewBox="0 0 12 8"><path d="M1 1l5 5 5-5" stroke="#333" stroke-width="1.5" fill="none"/></svg>
    </div>
  </div>

  <div class="grid">
    <div class="col">
      <article class="card">
        <div class="thumb t-green" role="img" aria-label="Illustration of a brain with a crossed-out sign"><span class="date">30<span>Nov</span></span></div>
        <div class="body"><div class="meta"><span>Idris Calloway</span><span>2 Comments</span></div>
          <h3>This is an Example of Sample Post</h3>
          <p>I searched a lot to find some cheap online training programs to get my 30 contact hours for the RMC...</p>
          <a class="more" href="#">Read More</a></div>
      </article>
      <article class="card">
        <div class="thumb t-blue" role="img" aria-label="Comparison graphic of two certifications with groups of people"><span class="date">30<span>Nov</span></span></div>
        <div class="body"><div class="meta"><span>Idris Calloway</span><span>2 Comments</span></div>
          <h3>STAGE9 vs PMC</h3>
          <p>Lorem Ipsum is simply dummy text of the printing and typesetting industry. make a type specimen book. It has survived not only five centuries,</p>
          <a class="more" href="#">Read More</a></div>
      </article>
    </div>

    <div class="col">
      <article class="card">
        <div class="body"><div class="meta"><span>Idris Calloway</span><span>2 Comments</span></div>
          <h3>30 Contact Hours Online RMC Training Programs</h3>
          <p>I searched a lot to find some cheap online training programs to get my 30 contact hours for the RMC...</p>
          <a class="more" href="#">Read More</a></div>
        <div class="thumb bottom t-orange" role="img" aria-label="Training program banner over a world map"><span class="date">30<span>Nov</span></span></div>
      </article>
      <article class="card">
        <div class="body"><div class="meta"><span>Idris Calloway</span><span>2 Comments</span></div>
          <h3>A List of Free PMC Mock Tests and Sample Questions</h3>
          <p>I searched a lot to find some cheap online training programs to get my 30 contact hours for the RMC...</p>
          <a class="more" href="#">Read More</a></div>
        <div class="thumb bottom t-paper" role="img" aria-label="Desk with laptop and phone, sample questions and mock tests title"><span class="date">30<span>Nov</span></span></div>
      </article>
    </div>

    <div class="col">
      <article class="card">
        <div class="thumb t-grey" role="img" aria-label="Process improvement title with a globe and improvement cycle"><span class="date">30<span>Nov</span></span></div>
        <div class="body"><div class="meta"><span>Idris Calloway</span><span>2 Comments</span></div>
          <h3>What is Delta Loop?</h3>
          <p>Lorem Ipsum is simply dummy text of the printing and typesetting industry. make a type specimen book. It has survived not only five centuries,</p>
          <a class="more" href="#">Read More</a></div>
      </article>
      <article class="card">
        <div class="thumb t-board" role="img" aria-label="Chalkboard reading lessons learned"><span class="date">30<span>Nov</span></span></div>
        <div class="body"><div class="meta"><span>Idris Calloway</span><span>2 Comments</span></div>
          <h3>RMC Exam : Lessons Learned by Renard Holt</h3>
          <p>I searched a lot to find some cheap online training programs to get my 30 contact hours for the RMC...</p>
          <a class="more" href="#">Read More</a></div>
      </article>
    </div>
  </div>

  <nav class="pager"><span class="nav">‹</span><span class="on">01</span><span>02</span><span>03</span><span>04</span><span class="nav">›</span></nav>
</section>

<section class="resources">
  <svg class="sweep" width="1200" height="853" viewBox="0 0 1200 853" aria-hidden="true">
    <path d="M0 420 C200 330 420 380 600 520 S1000 760 1200 700 L1200 853 L0 853Z" fill="#fff" opacity=".8"/>
  </svg>
  <h2>Top Recommended <b>Resources</b></h2>
  <p class="lead">Lorem ipsum dolor sit amet, consectetur adipiscing elit, sed do eiusmod<br>tempor incididunt ut labore et dolore magna aliqua.</p>
  <div class="products">
    <div class="product">
      <div class="ph" style="background:#9b9b9b"></div>
      <h3>The PMC Training Program</h3>
      <div class="by">By Idris Calloway</div>
      <p>Lorem ipsum dolor sit amet, consectetur adipiscing elit, sed do eiusmod tempor inci-didunt ut labore et</p>
      <a class="go" href="#"><svg width="18" height="12" viewBox="0 0 18 12"><path d="M1 6h15M11 1l5 5-5 5" stroke="#fff" stroke-width="2" fill="none"/></svg></a>
    </div>
    <div class="product">
      <div class="ph" style="background:#b8b8b8"></div>
      <h3>The PMC Training Program</h3>
      <div class="by">By Idris Calloway</div>
      <p>Lorem ipsum dolor sit amet, consectetur adipiscing elit, sed do eiusmod tempor inci-didunt ut labore et</p>
      <a class="go" href="#"><svg width="18" height="12" viewBox="0 0 18 12"><path d="M1 6h15M11 1l5 5-5 5" stroke="#fff" stroke-width="2" fill="none"/></svg></a>
    </div>
  </div>
</section>

<footer class="site-footer">
  <div class="f-cols">
    <div class="f-col contact">
      <h4>Contact Us</h4>
      <ul>
        <li><svg width="16" height="18" viewBox="0 0 16 18"><path d="M8 17s6-6 6-10A6 6 0 0 0 2 7c0 4 6 10 6 10z" stroke="#ddd" fill="none"/><circle cx="8" cy="7" r="2" stroke="#ddd" fill="none"/></svg><span>48 Marlow Lane #3<br>Dunmere 40112</span></li>
        <li><svg width="18" height="18" viewBox="0 0 18 18"><path d="M4 2l3 3-2 2c1 2 3 4 5 5l2-2 3 3-2 3C8 15 3 10 2 4z" stroke="#ddd" fill="none"/></svg><span>(555) 010-0420</span></li>
        <li><svg width="16" height="18" viewBox="0 0 16 18"><rect x="1" y="4" width="14" height="10" stroke="#ddd" fill="none"/><path d="M1 4l7 6 7-6" stroke="#ddd" fill="none"/></svg><span>hello@velrunok.com</span></li>
      </ul>
    </div>
    <div class="f-col links">
      <h4>Quick Links</h4>
      <ul><li>Home</li><li>PMC</li><li>Contact Hours</li><li>Resources</li><li>Notes</li><li>ebook</li></ul>
    </div>
    <div class="f-col write">
      <h4>WRITE TO US</h4>
      <p>Provide your email below to subscribe to our newsletter</p>
      <div class="sub"><div class="field">Email address</div><div class="btn">Subscribe</div></div>
    </div>
  </div>
  <div class="f-bottom">
    <span>Copyright 2020 velrunok. All rights reserved.</span>
    <div class="social"><i></i><i></i><i></i><i></i><i></i></div>
  </div>
</footer>

</body>
</html>
```